Builders Worksite Corflute Outdoor Sign

We are a building company who are just branching out into new construction. How first new build is our own home which was designed by us and a local architect. We are proud and want to create more advertisement around our business.

We need a corflute sign that can staked outside the construction site and can be seen by people passing by.
Updates

Can we please make the company name and logo bigger (Tidewater Ridge Homes) This needs to be the focus. Can we please replace 'Manu' with 'Contact Us on 021-574-3619'

Target Market(s)

Home owners and people wishing to build on lifestyle blocks in New Zealand.

Font styles to use
Sans Serif

Requirements
Must have
• It needs to feature our:
Logo
Company name
Contact name and number - Manu - 0215743619
Landscape NOT portrait.

```html
<!DOCTYPE html>
<html lang="en">
<head>
<meta charset="utf-8">
<title>Tidewater Ridge Homes – Site Sign</title>
<link rel="stylesheet" href="https://fonts.googleapis.com/css2?family=Barlow+Condensed:wght@700&family=Rubik:wght@600&display=swap">
<style>
  :root {
    --navy: #19202e;
    --gold: #edb920;
    --white: #ffffff;
  }
  html, body {
    margin: 0;
    padding: 0;
    width: 1200px;
    height: 896px;
    overflow: hidden;
    background: var(--white);
  }
  .sign {
    position: relative;
    width: 1200px;
    height: 896px;
    overflow: hidden;
  }
  .sign-panels {
    position: absolute;
    inset: 0;
    width: 1200px;
    height: 896px;
  }
  .brand-mark {
    position: absolute;
    left: 96px;
    top: 300px;
    width: 300px;
    display: flex;
    flex-direction: column;
    align-items: center;
    gap: 18px;
  }
  .brand-mark__dot {
    width: 112px;
    height: 112px;
    border-radius: 50%;
    background: var(--gold);
  }
  .brand-mark__name {
    font-family: "Barlow Condensed", sans-serif;
    font-weight: 700;
    font-size: 44px;
    line-height: 0.95;
    text-transform: uppercase;
    color: var(--navy);
    text-align: center;
    margin: 0;
  }
  .company-name {
    margin: 0;
    font-family: "Barlow Condensed", sans-serif;
    font-weight: 700;
    text-transform: uppercase;
    color: var(--white);
  }
  .company-name__line {
    position: absolute;
    left: 600px;
    right: 40px;
    display: flex;
    align-items: center;
    font-size: 132px;
    line-height: 1;
    letter-spacing: 1px;
  }
  .company-name__line--top { top: 0; height: 289px; }
  .company-name__line--mid { top: 289px; height: 214px; }
  .company-name__line--low { top: 503px; height: 230px; }
  .contact-bar {
    position: absolute;
    left: 0;
    top: 733px;
    width: 1200px;
    height: 163px;
    box-sizing: border-box;
    padding: 0 60px;
    display: flex;
    align-items: center;
    justify-content: center;
    gap: 22px;
    font-family: "Rubik", sans-serif;
    font-weight: 600;
    line-height: 1;
    color: var(--navy);
    white-space: nowrap;
  }
  .contact-bar__label {
    font-size: 44px;
    letter-spacing: 1px;
  }
  .contact-bar__icon {
    width: 62px;
    height: 62px;
    flex: none;
  }
  .contact-bar__number {
    font-size: 78px;
    letter-spacing: 1px;
  }
</style>
</head>
<body>
  <main class="sign">
    <svg class="sign-panels" viewBox="0 0 1462 1032" preserveAspectRatio="none" aria-hidden="true">
      <rect x="0" y="0" width="1462" height="845" fill="var(--navy)"/>
      <polygon fill="var(--gold)" points="0,0 355,0 650,333 1462,333 1462,580 720,580 598,845 0,845"/>
      <polygon fill="var(--navy)" points="280,0 330,0 630,333 580,333"/>
      <polygon fill="var(--navy)" points="672,580 702,580 578,845 546,845"/>
      <polygon fill="var(--white)" points="0,0 258,0 693,483 525,845 0,845"/>
      <rect x="0" y="845" width="1462" height="187" fill="var(--gold)"/>
    </svg>

    <div class="brand-mark">
      <div class="brand-mark__dot"></div>
      <p class="brand-mark__name">Tidewater<br>Ridge<br>Homes</p>
    </div>

    <h1 class="company-name">
      <span class="company-name__line company-name__line--top">Tidewater</span>
      <span class="company-name__line company-name__line--mid">Ridge</span>
      <span class="company-name__line company-name__line--low">Homes</span>
    </h1>

    <div class="contact-bar">
      <span class="contact-bar__label">CONTACT US ON</span>
      <svg class="contact-bar__icon" viewBox="0 0 100 100" aria-hidden="true">
        <circle cx="50" cy="50" r="45" fill="none" stroke="var(--navy)" stroke-width="7"/>
        <path fill="var(--navy)" d="M38 24c3-2 6-1 7 2l4 9c1 3 0 5-2 6l-4 2c-1 1-1 3 0 5l6 11c1 2 3 2 4 1l4-2c2-1 5 0 6 2l5 8c1 3 0 5-2 7l-4 3c-4 2-10 1-14-4C44 66 37 54 34 44c-2-7-1-14 3-18z"/>
      </svg>
      <span class="contact-bar__number">021-574-3619</span>
    </div>
  </main>
</body>
</html>
```